Technology research organisation needs a white paper redesign

Goal: Redesign the current "Platform Compass" white paper using our Pellara Insights branding.
- The design should promote a brand which is independent, has trusted advisors, is down to earth, has plain english advice based on solid research.
- Prefer a one column layout which is easy to read and has enough space for call outs on either left or right hand side.
- A4 size document will be distributed in PDF format
- Feel free to re-design existing graphs, tables, change images, headers and footers.
- Audience: HR Directors, CIO's & CFO's
- Must use our standard colour palette, see attached.
- The font used is company name: Frutiger LT 57 CN
- Should be inline with our website: pellarainsights.com.au
Design must allow for:
* Front Page
* Main content
* Contact details, about Pellara Insights & author example content can be found http://pellarainsights.com.au/about/
Output:
- All adobe design files
- Images, Fonts
Target Market(s)
Audience: HR Directors, CIO's & CFO's most likely 40+
Industry/Entity Type
It Company
Font styles to use
Other font styles liked:
- Frutiger LT 57 CN
Look and feel

```html
<!DOCTYPE html>
<html lang="en">
<head>
<meta charset="utf-8">
<title>HR/Payroll Software Selection – Pellara Insights</title>
<link href="https://fonts.googleapis.com/css2?family=Open+Sans:wght@400;600;700&family=Jost:wght@400;500&display=swap" rel="stylesheet">
<style>
  :root {
    --stage: #383838;
    --lime: #c5d328;
    --lime-deep: #8fae2a;
    --red: #e8412c;
    --red-deep: #9b2a1c;
    --ink: #333333;
    --text: #1f1f1f;
    --white: #ffffff;
  }
  * { margin: 0; padding: 0; box-sizing: border-box; }
  html, body { width: 1200px; height: 999px; overflow: hidden; background: var(--stage); }
  body { position: relative; font-family: "Open Sans", Arial, sans-serif; }

  .page { position: absolute; top: 120px; width: 553px; height: 736px; overflow: hidden; }

  /* Cover */
  .cover { left: 40px; background: var(--white); }
  .cover-photo { position: absolute; inset: 0;
    background: linear-gradient(160deg, #dfe6d6 0%, #b9c98c 35%, #7f8a6e 60%, #c9cfc8 80%, #a7b28e 100%); }
  .cover-shapes { position: absolute; inset: 0; }
  .brand { position: absolute; left: 22px; top: 38px; display: flex; align-items: center; gap: 8px; }
  .brand-dot { width: 30px; height: 30px; border-radius: 50%; background: var(--red); }
  .brand-name { font-family: "Open Sans", sans-serif; font-weight: 700; font-size: 19px; color: var(--ink); letter-spacing: .5px; text-transform: uppercase; }
  .title-band { position: absolute; left: 0; top: 564px; width: 250px; height: 43px; background: rgba(155,42,28,.85); }
  .cover-title { position: absolute; left: 19px; top: 510px; color: var(--white); font-size: 38px; line-height: 51px; font-weight: 400; }
  .cover-title strong { font-weight: 700; display: block; }
  .cover-sub { position: absolute; left: 22px; top: 664px; color: var(--white); font-size: 16px; line-height: 22px; font-weight: 600; }
  .cover-copy { position: absolute; left: 24px; top: 716px; color: var(--white); font-size: 11px; }

  /* Content page */
  .content { left: 625px; width: 551px; background: var(--white); }
  .content-shapes { position: absolute; inset: 0; }
  .content h1 { position: absolute; left: 26px; top: 28px; font-size: 29px; font-weight: 400; color: var(--ink); }
  .content h1 span { color: var(--red); font-weight: 700; }
  .intro { position: absolute; left: 27px; top: 78px; width: 440px; font-size: 13px; line-height: 18px; color: var(--ink); }
  .imperatives { position: absolute; left: 73px; top: 130px; list-style: none; font-family: "Jost", sans-serif; font-size: 13.5px; color: var(--text); }
  .imperatives li { height: 24.5px; display: flex; align-items: center; gap: 14px; }
  .imperatives li::before { content: ""; width: 10px; height: 10px; border-radius: 50%; background: var(--red); }
  .body-copy { position: absolute; left: 84px; top: 212px; width: 402px; font-family: "Jost", sans-serif; font-size: 13px; line-height: 24.5px; color: var(--text); text-align: justify; }
  .body-copy p + p { margin-top: 24.5px; }
  .footer-bar { position: absolute; left: 0; top: 695px; width: 411px; height: 21px; background: var(--red); color: var(--white); font-size: 10px; line-height: 21px; padding-left: 15px; }
  .footer-brand { position: absolute; left: 420px; top: 696px; display: flex; align-items: center; gap: 5px; }
  .footer-brand .brand-dot { width: 14px; height: 14px; }
  .footer-brand .brand-name { font-size: 9px; }
</style>
</head>
<body>
  <section class="page cover">
    <div class="cover-photo" role="img" aria-label="Photo of a smiling businesswoman holding a tablet in a bright office"></div>
    <svg class="cover-shapes" width="553" height="736" viewBox="0 0 553 736">
      <polygon points="443,0 553,0 553,300" fill="rgba(240,242,238,.85)"/>
      <polygon points="0,250 0,736 300,736" fill="rgba(143,174,42,.75)"/>
      <polygon points="553,500 553,736 470,736" fill="rgba(197,211,40,.7)"/>
    </svg>
    <div class="brand"><span class="brand-dot"></span><span class="brand-name">Pellara Insights</span></div>
    <div class="title-band"></div>
    <h1 class="cover-title">HR/Payroll<strong>Software</strong>Selection</h1>
    <p class="cover-sub">Navigating the marketplace and<br>choosing the right solution</p>
    <p class="cover-copy">Copyright Pellara Insights 2013</p>
  </section>

  <section class="page content">
    <svg class="content-shapes" width="551" height="736" viewBox="0 0 551 736">
      <polygon points="0,0 38,0 95,736 0,736" fill="var(--lime)"/>
      <polygon points="475,0 551,0 551,585" fill="var(--lime)"/>
    </svg>
    <h1>Challenges facing <span>HR/Payroll</span></h1>
    <p class="intro">The 2012 Corvale CEO Survey found three imperatives that are essential for high performing organisations:</p>
    <ul class="imperatives">
      <li>Empowering employees through values</li>
      <li>Engaging customers as individuals</li>
      <li>Amplifying innovation with partnerships</li>
    </ul>
    <div class="body-copy">
      <p>Two out of the above three require organisations to leverage their most important asset - people. Not surprisingly, 71% of CEOs see their people as a key source of sustained economic value.<br>Being able to successfully leverage an organisation workforce is key to the success of an HR Executive.</p>
      <p>In its 2013 report on HR Strategic Effectiveness, the UK’s Centre for Workforce Studies found that 85% of all organisations experienced difficulties in quantifying HR’s business impact. With only 43% able to forecast future workforce needs!</p>
      <p>Unfortunately the rest of the organisation is noticing HR’s inability to meet the needs of the business. A recent report by the Meridian Intelligence Unit, co-sponsored by Stratos and Corvale, found only 67% of CEOs were confident in the ability of HR Directors to lead their function, and only 42% of CFOs felt the same.</p>
    </div>
    <div class="footer-bar">01</div>
    <div class="footer-brand"><span class="brand-dot"></span><span class="brand-name">Pellara Insights</span></div>
  </section>
</body>
</html>
```